・大阪らしい闊達で明るいイメージ
・2025年開催予定のひかり環境博覧祭に向けて変わっていく新しい大阪のイメージ
・一目で南学競のパンフレットとわかるようなデザイン
・コロナ禍からの復活の象徴となる、ハンパなく熱い大会を彷彿とさせるデザイン
にしたいと思ってます。オリジナル・未発表の作品でお願い致します。

また、記載項目といたしまして
・表紙には以下の4項目を必ず記載してください。
1. 燃えまくり!!南学競
※阪には「はん」と上にふりがなをつけてください
※ぇは小さい「え」です
2. 開催日程:2023年7月31日(月)~8月25日(金)
3. 第75回南部医療学徒連合競技祭
4. 代表主管校:緑丘学院大学
・裏表紙には以下の2項目を必ず記載してください。
1. 〒999-0412 大阪府吹田市桜野台9丁目4 緑丘学院大学第75回南学競運営室
2. 第75回南部医療学徒連合競技祭運営委員会
B5
4ページ
• イラストレーター形式 (.ai)
・ページ数は4ページとしておりますが、デザインがそろっていれば何ページでも構いません。
・イラストはイラストレーター形式にて縦長仕様でお願いします。
・そのまま印刷会社に入稿するので、カラーモードはCMYKにて、塗り足し・アウトライン化もお願いします。
・ご提案を選択後、当選者様に修正を依頼する可能性がございますのでご了承ください。
・選択させていただいたデザインの著作権(財産権)等の扱いはDraftora利用規約に従い、弊運営委員会への譲渡をお願いします。
・以下に過去大会の総合パンフレットデザインを添付いたします。
・その他、何かご不明な点などございましたら、お気軽にご相談ください。
第72回、70回南学競のパンフレットデザインを添付いたします。

・「燃えまくり!!南学競」のスローガンに合う明るく勢いのあるデザイン
・一目で体育大会のポスターだとわかるデザイン
・星影の柱は緑丘学院大学(吹田キャンパス)の近くにあり、主管校の地域を反映したデザインになっている
・ポスター、パンフレットの表紙にふさわしい、シンプルながらも目をひくデザイン
・修正の依頼にもご丁寧に対応していただき、よりよいデザインに仕上げてくださった

以上の点からぴの様のデザインを選ばせていただきました。

たくさんのご応募をいただき、心より感謝申し上げます。
当選作品を選ぶのが非常に困難でしたが、どれも素晴らしいデザインでした。
来年も南学競のポスター・パンフレットデザインを募集することがあるかもしれません。
その際は、ぜひまたみなさまのご応募をお待ちしております。

今回のご参加、そして素晴らしい作品をご提案していただき、誠にありがとうございました。

```html
<!DOCTYPE html>
<html lang="ja">
<head>
<meta charset="utf-8">
<title>第75回 南部医療学徒連合競技祭</title>
<link rel="stylesheet" href="https://fonts.googleapis.com/css2?family=Shippori+Mincho+B1:wght@500;700;800&display=swap">
<style>
  :root {
    --paper: #f4ecdd;
    --orange: #e47f2a;
    --orange-deep: #d5651c;
    --ink-light: #fffaf2;
  }
  * { box-sizing: border-box; margin: 0; padding: 0; }
  html, body { width: 848px; height: 1200px; overflow: hidden; }
  body {
    font-family: "Shippori Mincho B1", "Noto Serif JP", serif;
    background: var(--paper);
  }
  .cover {
    position: relative;
    width: 848px;
    height: 1200px;
    overflow: hidden;
    background:
      radial-gradient(ellipse at 30% 20%, rgba(228,127,42,0.18), transparent 55%),
      radial-gradient(ellipse at 75% 80%, rgba(228,127,42,0.14), transparent 50%),
      var(--paper);
  }
  .athletes-art {
    position: absolute;
    left: 150px; top: 40px;
    width: 520px; height: 860px;
    border-radius: 40% 45% 38% 42%;
    background:
      radial-gradient(circle at 30% 30%, rgba(231,76,120,0.55), transparent 40%),
      radial-gradient(circle at 70% 25%, rgba(64,140,220,0.5), transparent 40%),
      radial-gradient(circle at 45% 65%, rgba(240,170,40,0.55), transparent 45%),
      radial-gradient(circle at 75% 70%, rgba(120,80,190,0.45), transparent 40%),
      radial-gradient(circle at 40% 90%, rgba(80,180,110,0.4), transparent 35%);
    filter: blur(6px);
  }
  .vertical { writing-mode: vertical-rl; text-orientation: upright; white-space: nowrap; }
  .edition {
    position: absolute;
    left: 16px; top: 16px;
    width: 128px; height: 50px;
    background: var(--orange);
    color: var(--ink-light);
    font-size: 28px; font-weight: 700;
    display: flex; align-items: center; justify-content: center;
    letter-spacing: 1px;
  }
  .title-main {
    position: absolute;
    left: 660px; top: 18px;
    color: var(--orange);
    font-size: 112px; font-weight: 800;
    line-height: 1;
    letter-spacing: 10px;
  }
  .title-sub {
    position: absolute;
    left: 24px; top: 175px;
    color: var(--orange);
    font-size: 128px; font-weight: 800;
    line-height: 1;
    letter-spacing: 22px;
  }
  .slogan {
    position: absolute;
    left: 362px; top: 255px;
    width: 104px; height: 460px;
    background: var(--orange-deep);
    color: var(--ink-light);
    display: flex; justify-content: center; align-items: center;
    font-size: 46px; font-weight: 700;
    line-height: 1.2;
    letter-spacing: 2px;
  }
  .slogan .tcy { text-combine-upright: all; }
  .slogan ruby rt { font-size: 14px; }
  .year {
    position: absolute;
    left: 150px; top: 938px;
    color: var(--orange);
    font-size: 32px; font-weight: 700;
  }
  .dates {
    position: absolute;
    left: 14px; top: 985px;
    color: var(--orange);
    font-weight: 700;
    display: flex; align-items: flex-end;
    line-height: 1;
    white-space: nowrap;
  }
  .dates .num { font-size: 124px; letter-spacing: -6px; }
  .dates .slash { font-size: 110px; margin: 0 2px; font-weight: 500; }
  .dates .dow { font-size: 26px; margin: 0 2px 12px 4px; }
  .dates .tilde { font-size: 60px; margin: 0 4px 34px; }
  .host {
    position: absolute;
    left: 650px; top: 965px;
    width: 170px; height: 205px;
    background: var(--orange);
    color: var(--ink-light);
    padding: 78px 14px 0;
  }
  .host .label { font-size: 15px; font-weight: 500; }
  .host .name { font-size: 21px; font-weight: 700; margin-top: 4px; white-space: nowrap; }
</style>
</head>
<body>
  <main class="cover">
    <div class="athletes-art" role="img" aria-label="Colourful watercolour silhouettes of athletes: volleyball, archery, badminton, basketball and other sports"></div>

    <div class="edition">第75回</div>

    <h1 class="title-main vertical">南部医療学徒</h1>
    <div class="title-sub vertical">連合競技祭</div>

    <div class="slogan vertical">
      <span><ruby>燃<rt>も</rt></ruby>えまくり<span class="tcy">!!</span>南学競</span>
    </div>

    <div class="year">2023年</div>
    <div class="dates">
      <span class="num">7</span><span class="slash">/</span><span class="num">31</span><span class="dow">(月)</span>
      <span class="tilde">~</span>
      <span class="num">8</span><span class="slash">/</span><span class="num">25</span><span class="dow">(金)</span>
    </div>

    <div class="host">
      <p class="label">代表主管校</p>
      <p class="name">緑丘学院大学</p>
    </div>
  </main>
</body>
</html>
```